Banner Design for High End Jewelry Website

We need a banner for our website (brindlestone.com) for a sale that we will be running. The banner should be a size 1187 × 400. I have included a few pieces of jewelry to be included in the banner (do not need to use all, can use just some). The banner should say:
"Christmas is Closer Than You Think Sale!"
Shop Now

Industry/Entity Type

Jewelry

```html
<!DOCTYPE html>
<html lang="en">
<head>
<meta charset="utf-8">
<title>Brindlestone — Fine Estate and Designer Jewelry</title>
<link href="https://fonts.googleapis.com/css2?family=Open+Sans:wght@400;600;700&display=swap" rel="stylesheet">
<style>
:root{
  --brown:#9c7f68;
  --brown-dark:#7a5c45;
  --band:#d4c5b4;
  --ink:#222;
  --muted:#666;
  --line:#ddd;
  --maroon:#6e1a10;
  --gold-text:#8a6a3a;
  --ribbon:#e8d4aa;
}
*{margin:0;padding:0;box-sizing:border-box}
html,body{width:1200px;height:1067px;overflow:hidden;background:#fff;font-family:'Open Sans',sans-serif;color:var(--ink)}
.page{position:relative;width:1200px;height:1067px}
.abs{position:absolute}
.util{top:14px;font-size:12.5px;letter-spacing:1px;color:#555;display:flex;align-items:center;gap:7px}
.util svg{width:16px;height:16px;stroke:#999;fill:none;stroke-width:1.4}
.brand{left:157px;top:52px;width:292px}
.brand-name{font-size:44px;font-weight:400;color:#111;letter-spacing:.5px;line-height:1}
.brand-tag{margin-top:28px;font-size:15px;color:#111;letter-spacing:.2px;white-space:nowrap}
.search{left:543px;top:62px;width:251px;height:23px;border-bottom:1px solid #999;display:flex;align-items:center}
.search svg{width:14px;height:14px;margin:0 12px 0 8px;stroke:#aaa;fill:none;stroke-width:1.5}
.search span{font-size:10.5px;color:#555;flex:1}
.search .go{width:25px;height:23px;background:var(--brown);display:flex;align-items:center;justify-content:center}
.search .go svg{margin:0;stroke:#fff;stroke-width:2.2}
.tool{top:50px;display:flex;flex-direction:column;align-items:center;gap:7px;font-size:10px;letter-spacing:1px;color:#555}
.tool svg{width:22px;height:20px;stroke:var(--brown);fill:none;stroke-width:1.3}
.nav{left:470px;top:111px;height:38px;display:flex;gap:1px}
.nav a{background:var(--brown);color:#fff;text-decoration:none;font-size:13.5px;letter-spacing:1px;display:flex;align-items:center;justify-content:center}
.ribbon{right:0;top:0;width:101px;height:100px}
.banner{left:156px;top:191px;width:890px;height:300px;background:radial-gradient(ellipse at 60% 40%,#fbf1de 0%,#f1e0bf 55%,#e6cf9f 100%)}
.headline{position:absolute;left:40px;top:82px;width:302px;text-align:center;line-height:1;font-size:36px}
.headline .l1{color:var(--maroon)}
.headline .l2{color:var(--gold-text);font-weight:400;margin-top:4px}
.headline .l3{color:var(--maroon);margin-top:4px}
.shop-now{position:absolute;left:133px;top:214px;width:116px;height:31px;background:#c58a3a;color:#fbe6b5;font-size:14px;display:flex;align-items:center;justify-content:center;box-shadow:0 2px 3px rgba(0,0,0,.2)}
.ph{position:absolute;border-radius:40%}
.arrivals{left:156px;top:525px;width:889px;height:342px;border:1px solid #e2e2e2;box-shadow:0 2px 3px rgba(0,0,0,.15)}
.arrivals-bar{height:44px;background:var(--band);display:flex;align-items:center;justify-content:center;position:relative}
.arrivals-title{font-size:23px;color:#fff;letter-spacing:1px}
.arrivals-title b{font-weight:400;background:var(--brown-dark);padding:0 2px}
.view-all{position:absolute;right:8px;top:7px;width:71px;height:31px;background:var(--brown-dark);color:#fff;font-size:11.5px;letter-spacing:.5px;display:flex;align-items:center;justify-content:center}
.product{position:absolute;top:52px;width:270px;text-align:center}
.product-name{font-size:10px;color:#444;height:34px;line-height:1.15}
.product-img{width:260px;height:168px;margin:0 auto;border-radius:6px}
.product-price{margin-top:36px;font-size:13.5px;font-weight:700;color:#444;letter-spacing:.5px}
.arrow{position:absolute;top:160px;width:17px;height:43px;background:#e4dcd4;display:flex;align-items:center;justify-content:center;box-shadow:1px 1px 2px rgba(0,0,0,.2)}
.arrow svg{width:9px;height:14px;stroke:#fff;fill:none;stroke-width:2}
.cat{top:876px;width:284px;height:191px;border:1px solid #e2e2e2}
.cat-img{height:150px;background:linear-gradient(135deg,#f6ebe0,#efdccd 60%,#f8efe6)}
.cat-label{height:40px;display:flex;align-items:center;justify-content:center;font-size:12.5px;letter-spacing:1.5px;color:#555}
</style>
</head>
<body>
<div class="page">

  <div class="abs util" style="left:584px">
    <svg viewBox="0 0 16 16"><path d="M3 2l3 1 1 3-2 1c1 2 2 3 4 4l1-2 3 1 1 3c-6 1-12-5-11-11z"/></svg>800 - 555 - 0142
  </div>
  <div class="abs util" style="left:755px">
    <svg viewBox="0 0 16 16"><path d="M2 6l3-3h6l3 3-6 7z M2 6h12"/></svg>SELL JEWELRY
  </div>
  <div class="abs util" style="left:909px;font-size:11px">
    <svg viewBox="0 0 16 16"><circle cx="8" cy="5" r="3"/><path d="M2 15c0-4 3-6 6-6s6 2 6 6z"/></svg>SIGN IN / REGISTER
  </div>

  <div class="abs brand">
    <div class="brand-name">Brindlestone</div>
    <div class="brand-tag">FINE ESTATE AND DESIGNER JEWELRY</div>
  </div>

  <div class="abs search">
    <svg viewBox="0 0 14 14"><circle cx="6" cy="6" r="4.5"/><path d="M9.5 9.5l3.5 3.5"/></svg>
    <span>Search</span>
    <div class="go"><svg viewBox="0 0 14 14"><path d="M3 7l3 3 5-6"/></svg></div>
  </div>

  <div class="abs tool" style="left:832px">
    <svg viewBox="0 0 22 20"><rect x="2" y="4" width="18" height="12"/><path d="M2 4l9 7 9-7"/></svg>NEWSLETTER
  </div>
  <div class="abs tool" style="left:926px">
    <svg viewBox="0 0 22 20"><path d="M11 18C4 12 2 9 2 6a4.5 4.5 0 0 1 9-1 4.5 4.5 0 0 1 9 1c0 3-2 6-9 12z"/></svg>WISHLIST
  </div>
  <div class="abs tool" style="left:1001px">
    <svg viewBox="0 0 22 20"><path d="M3 3h3l2 10h10l2-7H7"/><circle cx="9" cy="17" r="1.3"/><circle cx="17" cy="17" r="1.3"/></svg>CART (0)
  </div>

  <nav class="abs nav">
    <a style="width:133px">FINE JEWELRY</a>
    <a style="width:119px">TIMEPIECES</a>
    <a style="width:132px">ACCESSORIES</a>
    <a style="width:116px">DESIGNERS</a>
    <a style="width:71px">SALE</a>
  </nav>

  <svg class="abs ribbon" viewBox="0 0 101 100">
    <polygon points="0,0 101,0 101,100" fill="var(--ribbon)"/>
    <text x="62" y="40" transform="rotate(45 62 40)" font-family="Open Sans, sans-serif" font-size="12" fill="#333" text-anchor="middle">Sign up!</text>
    <polygon points="78,18 85,22 81,25" fill="#222"/>
  </svg>

  <section class="abs banner">
    <div class="headline">
      <div class="l1">CHRISTMAS is</div>
      <div class="l2">Closer Thank You</div>
      <div class="l3">THINK SALE!</div>
    </div>
    <div class="shop-now">SHOP NOW</div>
    <div class="ph" role="img" aria-label="Pair of gold figure-eight earrings with emerald and ruby cabochons" style="left:382px;top:62px;width:120px;height:103px;background:radial-gradient(circle,#8a6a2a,#d8b25a 60%,transparent 72%)"></div>
    <div class="ph" role="img" aria-label="Gold scale-pattern bangle bracelet with diamonds" style="left:502px;top:111px;width:151px;height:152px;background:radial-gradient(circle,#d39a3a,#b47a25 50%,transparent 72%)"></div>
    <div class="ph" role="img" aria-label="Enamelled gold brooch with ruby centre" style="left:702px;top:125px;width:103px;height:93px;background:radial-gradient(circle,#9a2020,#c08a35 40%,#3a3020 60%,transparent 72%)"></div>
  </section>

  <section class="abs arrivals">
    <div class="arrivals-bar">
      <div class="arrivals-title">NEW <b>ARRIVALS</b></div>
      <div class="view-all">VIEW ALL</div>
    </div>
    <div class="product" style="left:27px">
      <div class="product-name">Verana 6.00 Carat Fancy Diamond 18k Gold Bangle Bracelet</div>
      <div class="product-img" role="img" aria-label="Gold bangle bracelet set with fancy brown diamonds" style="background:radial-gradient(ellipse at center,#a08050 0%,#d9cbb5 30%,#fff 60%)"></div>
      <div class="product-price">$6,000</div>
    </div>
    <div class="product" style="left:308px">
      <div class="product-name">Castellane Spira Diamond Tourmaline 18 Karat Rose Gold Ring</div>
      <div class="product-img" role="img" aria-label="Rose gold coiled ring with diamonds and a red tourmaline" style="background:radial-gradient(ellipse at center,#c8876a 0%,#e8cfc2 35%,#fff 65%)"></div>
      <div class="product-price">$8,800</div>
    </div>
    <div class="product" style="left:590px">
      <div class="product-name">Art Deco Carved Emerald Ruby Diamond Platinum Brooch</div>
      <div class="product-img" role="img" aria-label="Platinum Art Deco brooch with carved emeralds and rubies" style="background:radial-gradient(ellipse at center,#7a8a7a 0%,#d6d8d4 30%,#fff 60%)"></div>
      <div class="product-price">$2,600</div>
    </div>
    <div class="arrow" style="left:1px"><svg viewBox="0 0 9 14"><path d="M7 1L2 7l5 6"/></svg></div>
    <div class="arrow" style="right:1px"><svg viewBox="0 0 9 14"><path d="M2 1l5 6-5 6"/></svg></div>
  </section>

  <div class="abs cat" style="left:156px">
    <div class="cat-img" role="img" aria-label="Platinum cushion-cut diamond halo ring"></div>
    <div class="cat-label">RINGS</div>
  </div>
  <div class="abs cat" style="left:456px">
    <div class="cat-img" role="img" aria-label="Gold earrings pavé set with pink sapphires"></div>
    <div class="cat-label">EARRINGS</div>
  </div>
  <div class="abs cat" style="left:758px">
    <div class="cat-img" role="img" aria-label="Wide gold bangle set with multicolour gemstones"></div>
    <div class="cat-label">BRACELETS</div>
  </div>

</div>
</body>
</html>
```